Word Templates for Green Energy Consulting Company

Please see attached brief. This is what we'd like. Please note that we have also launched a PowerPoint template project and we want the two designs to be consistent. We encourage designers to submit to both contests. PowerPoint project is here: https://www.plintorava.com/manage-project/brief/5183620

Font styles to use
Serif
Sans Serif

```html
<!DOCTYPE html>
<html lang="en">
<head>
<meta charset="utf-8">
<title>Solvane Group – Document Template</title>
<link href="https://fonts.googleapis.com/css2?family=Roboto:wght@400;500;700&display=swap" rel="stylesheet">
<style>
:root{
  --bg:#e9f4da;
  --navy:#22304a;
  --lime:#8cc63f;
  --green:#2f8f2f;
  --green-dark:#1f7a22;
  --blue:#1f7bc0;
  --text:#454545;
  --paper:#ffffff;
  --rule:#22304a;
}
*{margin:0;padding:0;box-sizing:border-box}
html,body{width:1200px;height:3167px;overflow:hidden}
body{background:var(--bg);font-family:'Roboto',Arial,sans-serif;color:var(--text);position:relative}
.page{position:absolute;left:102px;width:996px;height:1422px;background:var(--paper);box-shadow:0 6px 24px rgba(34,48,74,.18);overflow:hidden}
.page--about{top:118px}
.page--services{top:1628px}
.page-top{position:absolute;left:0;top:0;width:100%;height:15px;background:var(--navy)}
.page-accent{position:absolute;left:0;top:15px}
.page-header{position:absolute;left:0;top:30px;width:100%;height:83px;border-bottom:2px solid var(--rule)}
.section-title{position:absolute;left:92px;top:28px;font-size:23px;font-weight:700;color:var(--navy);letter-spacing:.2px}
.brand{position:absolute;right:98px;top:26px;display:flex;align-items:center;gap:8px}
.brand-mark{width:16px;height:16px;border-radius:50%;background:var(--lime)}
.brand-name{font-size:22px;font-weight:700;color:var(--navy)}
.heading{position:absolute;left:92px;font-weight:700}
.heading--main{top:148px;font-size:31px;color:var(--lime);letter-spacing:.3px}
.heading--sub{top:198px;font-size:21px;color:var(--blue);font-weight:500}
.body-copy{position:absolute;left:92px;width:810px;top:258px;font-size:14.6px;line-height:24.8px;text-align:justify}
.bullets{list-style:none}
.bullets li{position:relative;padding-left:41px;margin-bottom:22px}
.bullets li::before{content:"";position:absolute;left:0;top:6px;width:13px;height:13px;border-radius:50%;background:var(--green-dark)}
.bullets li::after{content:"";position:absolute;left:3px;top:10.5px;width:5px;height:5px;border-top:2px solid #fff;border-right:2px solid #fff;transform:rotate(45deg)}
.paragraphs{letter-spacing:.28px}
.paragraphs p{margin-bottom:26px}
.cards{position:absolute;left:92px;top:786px;display:flex;gap:27px}
.card{width:252px;height:405px;border:2px solid var(--lime);border-radius:4px 24px 24px 24px;text-align:center;box-shadow:0 6px 14px rgba(0,0,0,.1);padding-top:20px}
.card:first-child{border-radius:0 24px 24px 0}
.card-icon{width:77px;height:77px;border-radius:50%;background:linear-gradient(180deg,var(--lime),var(--green));margin:0 auto;display:flex;align-items:center;justify-content:center}
.card-title{margin-top:33px;font-size:16.5px;font-weight:500;color:var(--navy)}
.card-title::after{content:"";display:block;width:28px;height:2px;background:var(--lime);margin:6px auto 0}
.card-text{margin:14px 18px 0;font-size:14.4px;line-height:24.4px}
.page-footer{position:absolute;left:0;bottom:0;width:100%;height:79px;background:var(--navy)}
.footer-accent{position:absolute;right:0;top:0}
.contact{position:absolute;top:20px;display:flex;align-items:center;gap:14px;color:#fff;font-size:15px;font-weight:500}
.contact--phone{left:92px}
.contact--mail{left:328px}
.contact-icon{width:38px;height:38px;border-radius:50%;background:linear-gradient(180deg,var(--lime),var(--green));display:flex;align-items:center;justify-content:center}
.contact-divider{position:absolute;left:300px;top:18px;width:1px;height:44px;background:#3a4862}
.social{position:absolute;right:93px;top:42px;display:flex;gap:6px}
.social span{width:26px;height:26px;border-radius:50%;border:1px solid var(--lime)}
</style>
</head>
<body>

<section class="page page--about">
  <div class="page-top"></div>
  <svg class="page-accent" width="334" height="15"><polygon points="0,0 334,0 320,15 0,15" fill="#8cc63f"/></svg>
  <header class="page-header">
    <h1 class="section-title">1. ABOUT US</h1>
    <div class="brand"><span class="brand-mark"></span><span class="brand-name">Solvane Group</span></div>
  </header>
  <h2 class="heading heading--main">1.1. WHO WE ARE</h2>
  <h3 class="heading heading--sub">1.1.1. Lorem Ipsum is simply dummy text</h3>
  <div class="body-copy">
    <ul class="bullets">
      <li>Lorem ipsum dolor sit amet, consectetur adipiscing elit, sed do eiusmod tempor incididunt ut labore et dolore magna aliqua. Ut enim ad minim veniam, quis nostrud exercitation ullamco laboris nisi ut aliquip ex ea commodo consequat. Duis aute irure dolor in reprehenderit in voluptate velit esse cillum dolore eu fugiat nulla pariatur. Excepteur sint occaecat cupidatat non officquis nostrud exercitation ullamco laboris nisi ut aliquip ex ea commodo consequat. Duis aute irure dolor in reprehenderit in voluptate velit esse cillum dolore eu fugiat nulla pariatur. Excepteur sint occaecat cupidatat non officia deserquis nostrud exercitation ullamco laboris nisi ut aliquip ex ea commodo consequat. Duis aute irure dolor in reprevoluptate velit esse cillum henderitea.</li>
      <li>Lorem ipsum dolor sit amet, consectetur adipiscing elit, sed do eiusmod tempor incididunt ut labore et dolore magna aliqua. Ut enim ad minim veniam, quis nostrud exercitation ullamco laboris nisi ut aliquip ex ea commodo consequat. Duis aute irure dolor in reprehenderit in voluptate velit esse cillum dolore eu fugiat nulla pariatur. Excepteur sint occaecat cupidatat non officquis nostrud exercitationea.</li>
      <li>Lorem ipsum dolor sit amet, consectetur adipiscing elit, sed do eiusmod tempor incididunt ut labore et dolore magna aliqua. Ut enim ad minim veniam, quis nostrud exercitation ullamco laboris nisi ut aliquip ex ea commodo consequat. Duis aute irure dolor in reprehenderit in voluptate velit esse cillum dolore eu fugiat nulla pariatur. Excepteur sint occaecat cupidatat non officquis nostrud exercitation ullamco laboris nisi ut aliquip ex ea commodo consequat. Duis aute irure dolor in reprehenderit in voluptate velit esse cillum dolore eu fugiat nulla pariatur. Excepteur sint occaecat cupidatat non officia deserquis nostrud exercitation ullamco laboris nisi ut aliquip ex ea commodo consequat. Duis aute irure dolor in reprevoluptate velit esse cillum henderitea.</li>
      <li>Lorem ipsum dolor sit amet, consectetur adipiscing elit, sed do eiusmod tempor incididunt ut labore et dolore magna aliqua. Ut enim ad minim veniam, quis nostrud exercitation ullamco laboris nisi ut aliquip ex ea commodo consequat. Duis aute irure dolor in reprehenderit in voluptate velit esse cillum dolore eu fugiat nulla pariatur. Excepteur sint occaecat cupidatat non officquis nostrud exercitationea.</li>
      <li>Lorem ipsum dolor sit amet, consectetur adipiscing elit, sed do eiusmod tempor incididunt ut labore et dolore magna aliqua. Ut enim ad minim veniam, quis nostrud exercitation ullamco laboris nisi ut aliquip ex ea commodo consequat. Duis aute irure dolor in reprehenderit in voluptate velit esse cillum dolore eu fugiat nulla pariatur. Excepteur sint occaecat cupidatat non officquis nostrud exercitation ullamco laboris nisi ut aliquip ex ea commodo consequat. Duis aute irure dolor in reprehenderit in voluptate velit esse cillum dolore eu fugiat nulla pariatur. Excepteur sint occaecat cupidatat non officia deserquis nostrud exercitation ullamco laboris nisi ut aliquip ex ea commodo consequat. Duis aute irure dolor in reprevoluptate velit esse cillum henderitea.</li>
      <li>Lorem ipsum dolor sit amet, consectetur adipiscing elit, sed do eiusmod tempor incididunt ut labore et dolore magna aliqua. Ut enim ad minim veniam, quis nostrud exercitation ullamco laboris nisi ut aliquip ex ea commodo consequat. Duis aute irure dolor in reprehenderit in voluptate velit esse cillum dolore eu fugiat nulla pariatur. Excepteur sint occaecat cupidatat non officquis nostrud exercitationea.</li>
    </ul>
  </div>
  <footer class="page-footer">
    <svg class="footer-accent" width="313" height="30"><polygon points="0,0 313,0 313,30 28,30" fill="#8cc63f"/></svg>
    <div class="contact contact--phone">
      <span class="contact-icon"><svg width="16" height="16" viewBox="0 0 24 24"><path fill="#fff" d="M6.6 10.8a15 15 0 0 0 6.6 6.6l2.2-2.2c.3-.3.7-.4 1-.2 1.1.4 2.3.6 3.6.6.6 0 1 .4 1 1V20c0 .6-.4 1-1 1A17 17 0 0 1 3 4c0-.6.4-1 1-1h3.5c.6 0 1 .4 1 1 0 1.3.2 2.5.6 3.6.1.3 0 .7-.2 1z"/></svg></span>
      +1 (555) 014 2736
    </div>
    <div class="contact-divider"></div>
    <div class="contact contact--mail">
      <span class="contact-icon"><svg width="16" height="12" viewBox="0 0 16 12"><rect x="0" y="0" width="16" height="12" rx="1.5" fill="#fff"/><path d="M1 1.5l7 5 7-5" fill="none" stroke="#2f8f2f" stroke-width="1.5"/></svg></span>
      info@solvanegroup.com
    </div>
    <div class="social"><span></span><span></span><span></span><span></span></div>
  </footer>
</section>

<section class="page page--services">
  <div class="page-top"></div>
  <svg class="page-accent" width="334" height="15"><polygon points="0,0 334,0 320,15 0,15" fill="#8cc63f"/></svg>
  <header class="page-header">
    <h1 class="section-title">1. OUR SERVICES</h1>
    <div class="brand"><span class="brand-mark"></span><span class="brand-name">Solvane Group</span></div>
  </header>
  <h2 class="heading heading--main">1.1. WHAT WE DO</h2>
  <h3 class="heading heading--sub">1.1.2. Lorem Ipsum is simply dummy text</h3>
  <div class="body-copy paragraphs">
    <p>Lorem ipsum dolor sit amet, consectetur adipiscing elit, sed do eiusmod tempor incididunt ut labore et dolore magna aliqua. Ut enim ad minim veniam, quis nostrud exercitation ullamco laboris nisi ut aliquip ex ea commodo consequat. Duis aute irure dolor in reprehenderit in voluptate velit esse cillum dolore eu fugiat nulla pariatur. Excepteur sint occaecat cupidatat non officquis nostrud exercitation ullamco laboris nisi ut aliquip ex ea commodo consequat. Duis aute irure dolor in reprehenderit in voluptate velit esse cillum dolore eu fugiat nulla pariatur. Excepteur sint occaecat cupidatat non officia deserquis nostrud exercitation ullamco laboris nisi ut aliquip ex ea commodo consequat. Duis aute irure dolor in reprevoluptate velit esse cillum henderitea.</p>
    <p>Lorem ipsum dolor sit amet, consectetur adipiscing elit, sed do eiusmod tempor incididunt ut labore et dolore magna aliqua. Ut enim ad minim veniam, quis nostrud exercitation ullamco laboris nisi ut aliquip ex ea commodo consequat. Duis aute irure dolor in reprehenderit in voluptate velit esse cillum dolore eu fugiat nulla pariatur. Excepteur sint occaecat cupidatat non officquis nostrud exercitation ullamco laboris nisi ut aliquip ex ea commodo consequat. Duis aute irure dolor in reprehenderit in voluptate velit esse cillum dolorea.</p>
    <p>Lorem ipsum dolor sit amet, consectetur adipiscing elit, sed do eiusmod tempor incididunt ut labore et dolore magna aliqua. Ut enim ad minim veniam, quis nostrud exercitation ullamco laboris nisi ut aliquip ex ea commodo consequat. Duis aute irure dolor in reprehenderit in voluptate velit esse cillum dolore eu fugiat nulla pariatur. Excepteur sint occaecat cupidatat non officquis nostrud exercitation ullamco laborisea.</p>
  </div>
  <div class="cards">
    <article class="card">
      <div class="card-icon"><svg width="40" height="40" viewBox="0 0 40 40" fill="none" stroke="#fff" stroke-width="2"><path d="M8 20a12 12 0 0 1 20-9M32 20a12 12 0 0 1-20 9"/><path d="M28 6v5h-5M12 34v-5h5"/><path d="M22 12l-6 9h6l-4 8" stroke-linejoin="round"/></svg></div>
      <h4 class="card-title">LOREM IPSUM</h4>
      <p class="card-text">Lorem ipsum dolor sit amet, co nsectetur adipiscing elit, sed do eiusmod tempor incididunt ut labore et dolore magna ali qua ut enim ad minim veniam, quis nostrud exercitation ullamco laboris nisi ut aliquip exea commodo.</p>
    </article>
    <article class="card">
      <div class="card-icon"><svg width="40" height="40" viewBox="0 0 40 40" fill="none" stroke="#fff" stroke-width="2" stroke-linecap="round"><circle cx="20" cy="13" r="5"/><path d="M6 16v10l8 8M34 16v10l-8 8M11 22l5 5M29 22l-5 5"/></svg></div>
      <h4 class="card-title">LOREM IPSUM</h4>
      <p class="card-text">Lorem ipsum dolor sit amet, co nsectetur adipiscing elit, sed do eiusmod tempor incididunt ut labore et dolore magna ali qua ut enim ad minim veniam, quis nostrud exercitation ullamco laboris nisi ut aliquip exea commodo.</p>
    </article>
    <article class="card">
      <div class="card-icon"><svg width="40" height="40" viewBox="0 0 40 40" fill="none" stroke="#fff" stroke-width="2" stroke-linecap="round"><circle cx="22" cy="14" r="4"/><path d="M22 4v3M22 21v3M12 14h3M29 14h3M15 7l2 2M27 19l2 2M15 21l2-2M27 9l2-2"/><path d="M6 28h8l5 2h8M6 34h16l10-6"/></svg></div>
      <h4 class="card-title">LOREM IPSUM</h4>
      <p class="card-text">Lorem ipsum dolor sit amet, co nsectetur adipiscing elit, sed do eiusmod tempor incididunt ut labore et dolore magna ali qua ut enim ad minim veniam, quis nostrud exercitation ullamco laboris nisi ut aliquip exea commodo.</p>
    </article>
  </div>
  <footer class="page-footer">
    <svg class="footer-accent" width="313" height="30"><polygon points="0,0 313,0 313,30 28,30" fill="#8cc63f"/></svg>
    <div class="contact contact--phone">
      <span class="contact-icon"><svg width="16" height="16" viewBox="0 0 24 24"><path fill="#fff" d="M6.6 10.8a15 15 0 0 0 6.6 6.6l2.2-2.2c.3-.3.7-.4 1-.2 1.1.4 2.3.6 3.6.6.6 0 1 .4 1 1V20c0 .6-.4 1-1 1A17 17 0 0 1 3 4c0-.6.4-1 1-1h3.5c.6 0 1 .4 1 1 0 1.3.2 2.5.6 3.6.1.3 0 .7-.2 1z"/></svg></span>
      +1 (555) 014 2736
    </div>
    <div class="contact-divider"></div>
    <div class="contact contact--mail">
      <span class="contact-icon"><svg width="16" height="12" viewBox="0 0 16 12"><rect x="0" y="0" width="16" height="12" rx="1.5" fill="#fff"/><path d="M1 1.5l7 5 7-5" fill="none" stroke="#2f8f2f" stroke-width="1.5"/></svg></span>
      info@solvanegroup.com
    </div>
    <div class="social"><span></span><span></span><span></span><span></span></div>
  </footer>
</section>

</body>
</html>
```